Start up in business consultancy needs a business card

We need the business card's layout (we have already the logo). Our business is concerned on consultancy services delivered to companies on the matter of sustainability. Business card should be enough essentials and professional style.

Side A with the following info:
logo + a space for the claim (still to identify) + website of the company

Side B with the following info:
Name of business card holder + title of the business card holder + address of the company + space for mobile number, phone number, fax number + e-mail of business card holder + graphic details around.

Target Market(s)

Business of any sector

Industry/Entity Type

Business Service

Contact Information for Business Card

Name of the company:
Pianoverde srl
Società Benefit

Address of the company:
Via Lucerna, 7
21047 - Saronno (VA)

Website:
www.pianoverde.it

Name of the BC' holder:
Luca Ferentino

Title:
Co-fondatore

Email:
luca@pianoverde.it

Mobile:
+39 348 915 2074
Phone:
+39 348 915 2074
Fax:
+39 348 915 2074

Font styles to use
Other font styles liked:
• new gothic

```html
<!DOCTYPE html>
<html lang="it">
<head>
<meta charset="utf-8">
<title>Pianoverde – biglietto da visita</title>
<link rel="stylesheet" href="https://fonts.googleapis.com/css2?family=Mulish:wght@300;400;700;800&display=swap">
<style>
  :root {
    --brand-blue: #4a72ad;
    --ink-blue: #3d64a6;
    --paper: #ffffff;
    --backdrop: #f3e3cc;
    --card-shadow: rgba(90, 60, 30, 0.18);
  }
  * { box-sizing: border-box; margin: 0; padding: 0; }
  html, body {
    width: 1200px; height: 800px; overflow: hidden;
    background: var(--backdrop);
    font-family: "Mulish", "Century Gothic", sans-serif;
  }
  .sheet {
    width: 1200px; height: 800px;
    display: flex; align-items: center; justify-content: center; gap: 60px;
  }
  .card {
    position: relative;
    width: 520px; height: 298px;
    box-shadow: 0 10px 30px var(--card-shadow);
    overflow: hidden;
  }

  /* Side B – holder details */
  .card--details { background: var(--paper); color: var(--ink-blue); }
  .card__rules { position: absolute; inset: 0; }
  .holder { position: absolute; left: 44px; top: 34px; }
  .holder__name {
    font-weight: 800; font-size: 23px; letter-spacing: 0.5px; text-transform: uppercase;
  }
  .holder__title { font-weight: 300; font-size: 20px; margin-top: 1px; }
  .contacts {
    position: absolute; left: 232px; top: 168px;
    list-style: none; font-size: 12.5px; line-height: 17px; font-weight: 400;
  }
  .contacts li { display: flex; align-items: center; gap: 8px; }
  .contacts svg { width: 11px; height: 11px; flex: none; }

  /* Side A – brand */
  .card--brand {
    background: linear-gradient(120deg, #3f68a6 0%, var(--brand-blue) 55%, #6589bd 100%);
    color: var(--paper);
  }
  .brand {
    position: absolute; left: 100px; top: 92px;
    display: flex; align-items: center; gap: 16px;
  }
  .brand__dot {
    width: 58px; height: 58px; border-radius: 50%;
    border: 3px solid var(--paper);
  }
  .brand__name { font-size: 36px; font-weight: 400; letter-spacing: 0.5px; }
  .brand__site {
    position: absolute; left: 100px; top: 186px;
    font-size: 15px; font-weight: 400; letter-spacing: 0.6px;
  }
</style>
</head>
<body>
<main class="sheet">

  <section class="card card--details" aria-label="Retro del biglietto">
    <svg class="card__rules" viewBox="0 0 520 298" aria-hidden="true">
      <line x1="290" y1="0" x2="277" y2="24" stroke="var(--ink-blue)" stroke-width="3"/>
      <line x1="14" y1="178" x2="150" y2="106" stroke="var(--ink-blue)" stroke-width="3"/>
    </svg>
    <div class="holder">
      <h1 class="holder__name">Luca Ferentino</h1>
      <p class="holder__title">Co-fondatore</p>
    </div>
    <ul class="contacts">
      <li>
        <svg viewBox="0 0 12 12"><path d="M6 1a3.5 3.5 0 0 0-3.5 3.5C2.5 7 6 11 6 11s3.5-4 3.5-6.5A3.5 3.5 0 0 0 6 1z" fill="none" stroke="currentColor"/><circle cx="6" cy="4.5" r="1.2" fill="currentColor"/></svg>
        Via Lucerna, 7 &nbsp;21047 - Saronno (VA)
      </li>
      <li>
        <svg viewBox="0 0 12 12"><rect x="1" y="2.5" width="10" height="7" fill="none" stroke="currentColor"/><path d="M1 2.5l5 4 5-4" fill="none" stroke="currentColor"/></svg>
        luca@pianoverde.it
      </li>
      <li>
        <svg viewBox="0 0 12 12"><rect x="3.5" y="1" width="5" height="10" rx="1" fill="none" stroke="currentColor"/><circle cx="6" cy="9.3" r="0.6" fill="currentColor"/></svg>
        +39 348 915 2074
      </li>
      <li>
        <svg viewBox="0 0 12 12"><path d="M2 2.5c1-1 2-1 2.6 0l.8 1.4c.3.6 0 1.1-.5 1.5 .6 1.2 1.5 2.1 2.7 2.7.4-.5.9-.8 1.5-.5l1.4.8c1 .6 1 1.6 0 2.6C7 12 0 5 2 2.5z" fill="none" stroke="currentColor"/></svg>
        +39 348 915 2074
      </li>
      <li>
        <svg viewBox="0 0 12 12"><rect x="1" y="4" width="10" height="6" fill="none" stroke="currentColor"/><rect x="3" y="1" width="6" height="3" fill="none" stroke="currentColor"/><line x1="3" y1="7.5" x2="9" y2="7.5" stroke="currentColor"/></svg>
        +39 348 915 2074
      </li>
    </ul>
  </section>

  <section class="card card--brand" aria-label="Fronte del biglietto">
    <div class="brand">
      <span class="brand__dot" aria-hidden="true"></span>
      <span class="brand__name">pianoverde</span>
    </div>
    <p class="brand__site">www.pianoverde.it</p>
  </section>

</main>
</body>
</html>
```